Velka Haven

Yoga and Pilates
I teach privates and small groups

Simple clean design 2-4 pages.
(Bookings will be though contacting me, so need for booking capabilities)

```html
<!DOCTYPE html>
<html lang="en">
<head>
<meta charset="utf-8">
<title>Velka Haven — Yoga and Pilates</title>
<link href="https://fonts.googleapis.com/css2?family=Allura&family=Poppins:wght@400;500;600;700&display=swap" rel="stylesheet">
<style>
:root{
  --green:#6a9a68;
  --green-dark:#2e5a2d;
  --green-light:#9cc39a;
  --ink:#1d1d1d;
  --text:#444;
  --muted:#777;
  --grey-bg:#f2f2f2;
  --footer:#231a16;
  --white:#fff;
  --script:'Allura',cursive;
  --sans:'Poppins',sans-serif;
}
*{box-sizing:border-box;margin:0;padding:0}
html,body{width:1200px;height:3769px;overflow:hidden}
body{font-family:var(--sans);color:var(--text);background:var(--white);position:relative}
section,header,footer{position:absolute;left:0;width:1200px}
.abs{position:absolute}
.script{font-family:var(--script);color:var(--green);font-weight:400;line-height:1}
.title{font-family:var(--sans);color:var(--ink);font-weight:700;line-height:1.1}
.para{font-size:13.5px;line-height:23px;color:var(--text)}
.btn{position:absolute;background:var(--green);color:var(--white);font-size:13px;font-weight:600;text-transform:uppercase;display:flex;align-items:center;justify-content:center;letter-spacing:.2px}
.center{left:0;width:1200px;text-align:center}

/* header */
.site-header{top:0;height:67px;background:rgba(30,30,30,.72);z-index:5}
.brand{left:158px;top:18px;display:flex;align-items:center;gap:10px;color:var(--white);font-size:22px;font-weight:500}
.brand-dot{width:22px;height:22px;border-radius:50%;background:var(--green-light)}
.nav a{position:absolute;top:23px;color:var(--white);font-size:13px;text-decoration:none}
.nav .active::after{content:"";position:absolute;left:50%;top:23px;width:8px;height:8px;margin-left:-4px;border-radius:50%;border:1px solid var(--green-light)}
.call{left:868px;top:12px;width:174px;height:42px;background:var(--green);color:var(--white);font-size:14px;display:flex;align-items:center;justify-content:center;gap:10px}

/* hero */
.hero{top:0;height:631px;background:linear-gradient(160deg,#6f655d 0%,#9a8f85 30%,#a59c92 50%,#7b6f66 75%,#4d3e3c 100%)}
.hero-shade{inset:0;background:rgba(0,0,0,.15)}
.hero-title{top:215px;font-family:var(--script);font-size:110px;color:var(--white);line-height:1}
.hero-sub{top:343px;font-size:23px;color:var(--white)}
.arrow-box{top:268px;width:79px;height:79px;background:rgba(106,154,104,.7);display:flex;align-items:center;justify-content:center}

/* appointment */
.appointment{top:631px;height:436px;background:var(--grey-bg)}
.calendar{left:158px;top:35px;width:351px;height:366px;background:var(--green);padding:13px}
.cal-inner{background:var(--white);width:100%;height:100%;position:relative}
.cal-month{left:0;width:100%;top:32px;text-align:center;font-size:15px;font-weight:600;color:var(--ink)}
.cal-next{right:14px;top:32px;font-size:14px;color:var(--ink)}
.cal-grid{left:1px;top:74px;display:grid;grid-template-columns:repeat(7,46px);grid-auto-rows:46.5px;font-size:12.5px;color:var(--ink)}
.cal-grid .dow{height:20px;font-size:10px;font-weight:500;display:flex;align-items:center;justify-content:center}
.cal-grid span{display:flex;align-items:center;justify-content:center}
.cal-grid .off{color:#c8c8c8}
.cal-grid .today{width:36px;height:36px;margin:auto;border:1.5px solid #3d8fe0;border-radius:50%}
.dow-row{display:contents}

/* about */
.about{top:1067px;height:486px;background:var(--white)}
.about-frame{left:588px;top:54px;width:432px;height:351px;background:var(--green)}
.about-photo{left:612px;top:76px;width:430px;height:353px;background:linear-gradient(135deg,#d9d6d2 0%,#bdb6ad 40%,#8e8a86 70%,#5d6670 100%)}
.play{left:797px;top:222px;width:60px;height:60px;border-radius:50%;background:#e24b4b;display:flex;align-items:center;justify-content:center}

/* classes */
.classes{top:1553px;height:603px;background:linear-gradient(135deg,#2b5a2a 0%,#376b34 50%,#2a5528 100%)}
.card{top:164px;width:282px;height:324px;background:var(--white);border-top-right-radius:36px;overflow:visible}
.card-photo{left:0;top:0;width:282px;height:193px;border-top-right-radius:36px;background:linear-gradient(160deg,#6c6f78,#a7a09a 55%,#5b524c)}
.card-pill{left:41px;top:171px;width:236px;height:41px;border-radius:21px;background:var(--green);color:var(--white);font-size:11.5px;display:flex;align-items:center;justify-content:center;gap:10px}
.card-pill i{width:1px;height:14px;background:rgba(255,255,255,.8)}
.card-script{top:225px;font-size:25px}
.card-title{top:252px;font-size:16.5px;font-weight:600;color:var(--ink)}
.card-sub{top:282px;font-size:12.5px;color:var(--text)}
.card .ctr{left:0;width:100%;text-align:center}

/* facilities */
.facilities{top:2156px;height:633px;background:var(--white)}
.halo{left:432px;top:160px;width:322px;height:322px;border-radius:50%;background:radial-gradient(circle,#fff 60%,#f1f1f1 100%)}
.figure{left:424px;top:194px;width:330px;height:440px;border-radius:165px 165px 40px 40px;background:linear-gradient(180deg,#e9dfd6 0%,#b39582 30%,#2a3348 60%,#1f2a44 100%)}
.fac-icon{width:90px;height:90px;border-radius:50%;background:var(--green);border:2px dashed rgba(255,255,255,.8);box-shadow:0 0 0 4px var(--green);display:flex;align-items:center;justify-content:center}
.fac-dot{width:14px;height:14px;border-radius:50%;background:var(--green-light)}
.fac-text{width:226px}
.fac-text h3{font-size:16.5px;font-weight:600;color:var(--ink);margin-bottom:10px}
.fac-text p{font-size:13px;line-height:23px}
.fac-left{text-align:right}

/* contact */
.contact{top:2789px;height:477px;background:var(--grey-bg)}
.info{left:158px;display:flex;gap:17px}
.info-icon{width:58px;height:58px;background:var(--green);display:flex;align-items:center;justify-content:center;flex:none}
.info h4{font-size:14px;font-weight:400;color:var(--ink);margin-top:5px}
.info p{font-size:14px;color:var(--muted);line-height:22px}
.field{background:var(--white);border:1.5px solid #c9c9c9;font-size:12px;color:#777;padding:12px 14px}

/* footer */
.site-footer{top:3266px;height:463px;background:radial-gradient(ellipse at 50% 25%,#4a3a2e 0%,#2a1f19 45%,#1c1512 100%)}
.site-footer .w{color:var(--white)}
.foot-h{font-size:15px;color:var(--white)}
.foot-h::after{content:"";display:block;width:42px;height:2px;background:var(--green);margin-top:6px}
.links li{list-style:none;position:absolute;font-size:13px;color:var(--white)}
.links li::before{content:"»";position:absolute;left:-29px;color:var(--white)}
.hours span{position:absolute;font-size:13.5px;color:var(--white)}
.hours .lbl{font-size:12px;color:var(--green-light)}
.insta{left:833px;top:157px;display:grid;grid-template-columns:repeat(3,65.6px);grid-auto-rows:52.6px;gap:6px}
.insta div{background:linear-gradient(135deg,#7d8fa6,#d39a6a)}
.insta div:nth-child(2n){background:linear-gradient(135deg,#b9b2a6,#6f7f68)}
.insta div:nth-child(3n){background:linear-gradient(135deg,#c8786a,#5a6f92)}
.mail{left:260px;top:314px;width:283px;height:42px;background:var(--white);font-size:13px;color:#555;padding:11px 18px}
.mail-go{left:504px;top:325px;width:28px;height:28px;border-radius:50%;background:var(--green);display:flex;align-items:center;justify-content:center}
.bottom-bar{top:3729px;height:40px;background:var(--green)}
.social{top:7px;width:26px;height:26px;border-radius:50%;background:var(--white)}
</style>
</head>
<body>

<header class="site-header">
  <div class="abs brand"><span class="brand-dot"></span>Velka Haven</div>
  <nav class="nav">
    <a href="#" class="active" style="left:472px">Home</a>
    <a href="#" style="left:568px">About</a>
    <a href="#" style="left:660px">Classes</a>
    <a href="#" style="left:764px">Contact</a>
  </nav>
  <div class="abs call">
    <svg width="22" height="22" viewBox="0 0 24 24" fill="none" stroke="#fff" stroke-width="1.6"><circle cx="12" cy="12" r="10.5"/><path d="M8.5 7.5c.5-.5 1.3-.4 1.6.2l.8 1.6c.2.4.1.9-.2 1.2l-.6.6c.6 1.4 1.6 2.4 3 3l.6-.6c.3-.3.8-.4 1.2-.2l1.6.8c.6.3.7 1.1.2 1.6l-.7.7c-.8.8-2 1-3 .5-2.3-1.1-4.1-2.9-5.2-5.2-.5-1-.3-2.2.5-3z" fill="#fff" stroke="none"/></svg>
    (555) 214-7730
  </div>
</header>

<section class="hero">
  <div class="abs" role="img" aria-label="Photo of a yoga instructor guiding a student in a seated forward stretch in a sunlit studio" style="inset:0"></div>
  <div class="abs hero-shade"></div>
  <div class="abs arrow-box" style="left:70px"><svg width="22" height="22" viewBox="0 0 24 24" fill="none" stroke="#fff" stroke-width="3.5"><path d="M15 4l-8 8 8 8"/></svg></div>
  <div class="abs arrow-box" style="left:1051px"><svg width="22" height="22" viewBox="0 0 24 24" fill="none" stroke="#fff" stroke-width="3.5"><path d="M9 4l8 8-8 8"/></svg></div>
  <h1 class="abs center hero-title">Velka Haven</h1>
  <p class="abs center hero-sub">Yoga Group Set Out To Reduce Anxiety</p>
  <a class="btn" style="left:512px;top:407px;width:174px;height:42px">Join Us Now</a>
</section>

<section class="appointment">
  <div class="abs calendar">
    <div class="cal-inner">
      <div class="abs cal-month">APRIL 2022</div>
      <div class="abs cal-next">→</div>
      <div class="abs cal-grid">
        <span class="dow">MON</span><span class="dow">TUE</span><span class="dow">WED</span><span class="dow">THU</span><span class="dow">FRI</span><span class="dow">SAT</span><span class="dow">SUN</span>
        <span class="off">28</span><span class="off">29</span><span class="off">30</span><span class="off">31</span><span class="off">1</span><span class="off">2</span><span class="off">3</span>
        <span><span class="today">4</span></span><span>5</span><span>6</span><span>7</span><span>8</span><span>9</span><span class="off">10</span>
        <span>11</span><span>12</span><span>13</span><span>14</span><span>15</span><span>16</span><span class="off">17</span>
        <span>18</span><span>19</span><span>20</span><span>21</span><span>22</span><span>23</span><span class="off">24</span>
        <span>25</span><span>26</span><span>27</span><span>28</span><span>29</span><span>30</span><span class="off">1</span>
      </div>
    </div>
  </div>
  <p class="abs script" style="left:593px;top:58px;font-size:44px">Make Easy To</p>
  <h2 class="abs title" style="left:593px;top:103px;font-size:36px">Book An Appointment</h2>
  <p class="abs para" style="left:593px;top:163px;width:450px">Not sure where to start? Let us help you out! Whether you've been stuck on the couch for the last ten years, or are looking to take your fitness to the next level, this is your program!</p>
  <p class="abs para" style="left:593px;top:257px;width:450px">Totam rem eaquiti sociosqu ad litora hendrerit in vulputate velit esse mol Mauris odio ilms it con nec a odio sequat auctor.</p>
  <a class="btn" style="left:594px;top:329px;width:204px;height:44px">Book An Appointment</a>
</section>

<section class="about">
  <p class="abs script" style="left:158px;top:85px;font-size:44px">Learn More</p>
  <h2 class="abs title" style="left:158px;top:129px;font-size:36px">About Velka Haven</h2>
  <p class="abs para" style="left:158px;top:189px;width:410px">Not sure where to start? Let us help you out! Whether you've been stuck on the couch for the last ten years, or are looking to take your fitness to the next level, this is your program!</p>
  <p class="abs para" style="left:158px;top:281px;width:420px">Totam rem eaquiti sociosqu ad litora hendrerit in vulputate velit esse mol Mauris odio ilms it con nec a odio sequat auctor.</p>
  <a class="btn" style="left:158px;top:351px;width:176px;height:44px">Read More</a>
  <div class="abs about-frame"></div>
  <div class="abs about-photo" role="img" aria-label="Video still of an instructor adjusting two students in downward dog in a bright studio"></div>
  <div class="abs play"><svg width="18" height="20" viewBox="0 0 18 20"><path d="M3 1l14 9-14 9z" fill="#fff"/></svg></div>
</section>

<section class="classes">
  <p class="abs center script" style="top:50px;font-size:44px;color:var(--white)">Physical, Mental, And Spiritual Practice</p>
  <h2 class="abs center title" style="top:98px;font-size:36px;color:var(--white)">Our Classes</h2>

  <article class="abs card" style="left:158px">
    <div class="abs card-photo" role="img" aria-label="Photo of a group class holding a warrior pose in a gym"></div>
    <div class="abs card-pill">
      <svg width="12" height="12" viewBox="0 0 12 12" fill="none" stroke="#fff" stroke-width="1.2"><rect x="1" y="2" width="10" height="9"/><path d="M1 5h10M4 1v2M8 1v2"/></svg>Mar 4 ,2022<i></i>
      <svg width="12" height="12" viewBox="0 0 12 12" fill="none" stroke="#fff" stroke-width="1.2"><circle cx="6" cy="6" r="5"/><path d="M6 3v3l2 1"/></svg>16:00 - 20:00
    </div>
    <p class="abs ctr script card-script">Many Desktop</p>
    <h3 class="abs ctr card-title">Publishing Packages</h3>
    <p class="abs ctr card-sub">25 / Number Of Week</p>
  </article>

  <article class="abs card" style="left:458px">
    <div class="abs card-photo" role="img" aria-label="Photo of a class doing side stretches on mats" style="background:linear-gradient(160deg,#8d7e78,#d98a4c 50%,#7a8a9a)"></div>
    <div class="abs card-pill">
      <svg width="12" height="12" viewBox="0 0 12 12" fill="none" stroke="#fff" stroke-width="1.2"><rect x="1" y="2" width="10" height="9"/><path d="M1 5h10M4 1v2M8 1v2"/></svg>Mar 4 ,2022<i></i>
      <svg width="12" height="12" viewBox="0 0 12 12" fill="none" stroke="#fff" stroke-width="1.2"><circle cx="6" cy="6" r="5"/><path d="M6 3v3l2 1"/></svg>16:00 - 20:00
    </div>
    <p class="abs ctr script card-script">Many Desktop</p>
    <h3 class="abs ctr card-title">Publishing Packages</h3>
    <p class="abs ctr card-sub">25 / Number Of Week</p>
  </article>

  <article class="abs card" style="left:758px">
    <div class="abs card-photo" role="img" aria-label="Photo of a seated meditation group with hands in prayer" style="background:linear-gradient(160deg,#8a7c70,#cbb9a2 50%,#6d7d5a)"></div>
    <div class="abs card-pill">
      <svg width="12" height="12" viewBox="0 0 12 12" fill="none" stroke="#fff" stroke-width="1.2"><rect x="1" y="2" width="10" height="9"/><path d="M1 5h10M4 1v2M8 1v2"/></svg>Mar 4 ,2022<i></i>
      <svg width="12" height="12" viewBox="0 0 12 12" fill="none" stroke="#fff" stroke-width="1.2"><circle cx="6" cy="6" r="5"/><path d="M6 3v3l2 1"/></svg>16:00 - 20:00
    </div>
    <p class="abs ctr script card-script">Many Desktop</p>
    <h3 class="abs ctr card-title">Publishing Packages</h3>
    <p class="abs ctr card-sub">25 / Number Of Week</p>
  </article>

  <a class="btn" style="left:512px;top:506px;width:174px;height:43px">View All Classes</a>
</section>

<section class="facilities">
  <p class="abs center script" style="top:38px;font-size:44px">Best Fasilites</p>
  <h2 class="abs center title" style="top:83px;font-size:36px">Of Velka Haven</h2>
  <div class="abs halo"></div>
  <div class="abs figure" role="img" aria-label="Photo of a woman meditating in lotus pose"></div>

  <div class="abs fac-icon" style="left:409px;top:173px"><svg width="44" height="44" viewBox="0 0 44 44" fill="none" stroke="#fff" stroke-width="2"><path d="M22 6c6 8 6 20 0 32-6-12-6-24 0-32z"/><path d="M22 38V18"/></svg></div>
  <div class="abs fac-dot" style="left:412px;top:170px"></div>
  <div class="abs fac-icon" style="left:695px;top:173px"><svg width="44" height="44" viewBox="0 0 44 44" fill="none" stroke="#fff" stroke-width="2"><circle cx="22" cy="20" r="7"/><path d="M22 6v5M22 29v5M8 20h5M31 20h5M12 10l3 3M32 10l-3 3M10 38h24"/></svg></div>
  <div class="abs fac-dot" style="left:760px;top:170px"></div>
  <div class="abs fac-icon" style="left:409px;top:360px"><svg width="44" height="44" viewBox="0 0 44 44" fill="none" stroke="#fff" stroke-width="2"><circle cx="22" cy="22" r="13"/><path d="M22 9v26M15 15c3 2 4 5 0 7M29 15c-3 2-4 5 0 7M15 29c3-2 5-2 7 0M29 29c-3-2-5-2-7 0"/></svg></div>
  <div class="abs fac-dot" style="left:412px;top:357px"></div>
  <div class="abs fac-icon" style="left:695px;top:360px"><svg width="44" height="44" viewBox="0 0 44 44" fill="none" stroke="#fff" stroke-width="2"><path d="M22 10c4 4 4 12 0 18-4-6-4-14 0-18zM10 18c6 0 10 5 12 10-6 0-11-4-12-10zM34 18c-6 0-10 5-12 10 6 0 11-4 12-10zM8 32h28"/></svg></div>
  <div class="abs fac-dot" style="left:760px;top:357px"></div>

  <div class="abs fac-text fac-left" style="left:157px;top:164px"><h3>Ashtanga Yoga</h3><p>Not sure where to start? Let us help you out! Whether you've been stuck on the couch</p></div>
  <div class="abs fac-text fac-left" style="left:157px;top:352px"><h3>Boosts your Memory</h3><p>Not sure where to start? Let us help you out! Whether you've been stuck on the couch</p></div>
  <div class="abs fac-text" style="left:814px;top:164px"><h3>Ashtanga Yoga</h3><p>Not sure where to start? Let us help you out! Whether you've been stuck on the couch</p></div>
  <div class="abs fac-text" style="left:814px;top:352px"><h3>Mediation Coaching</h3><p>Not sure where to start? Let us help you out! Whether you've been stuck on the couch</p></div>
</section>

<section class="contact">
  <p class="abs script" style="left:155px;top:78px;font-size:44px">Would You Like</p>
  <h2 class="abs title" style="left:156px;top:124px;font-size:34px">Discuss A Yoga?</h2>

  <div class="abs info" style="top:180px">
    <div class="info-icon"><svg width="22" height="16" viewBox="0 0 22 16" fill="none" stroke="#fff" stroke-width="1.8"><rect x="1" y="1" width="20" height="14"/><path d="M1 1l10 8 10-8"/></svg></div>
    <div><h4>Email</h4><p>hello@velkahaven.com</p></div>
  </div>
  <div class="abs info" style="top:252px">
    <div class="info-icon"><svg width="20" height="20" viewBox="0 0 24 24"><path d="M6 2c.7-.6 1.7-.4 2.1.4l1.5 3c.3.6.2 1.3-.3 1.7l-1.2 1.1c1.1 2.6 3 4.5 5.6 5.6l1.1-1.2c.4-.5 1.1-.6 1.7-.3l3 1.5c.8.4 1 1.4.4 2.1l-1.5 1.7c-1 1.1-2.6 1.4-3.9.8C9.4 16.6 7.3 14.6 5.5 11 4.9 9.7 5.2 8.1 6.3 7.1z" fill="#fff"/></svg></div>
    <div><h4>Phone</h4><p>0555-210-384</p></div>
  </div>
  <div class="abs info" style="top:324px">
    <div class="info-icon"><svg width="18" height="24" viewBox="0 0 18 24"><path d="M9 0C4 0 0 4 0 9c0 6.5 9 15 9 15s9-8.5 9-15c0-5-4-9-9-9zm0 12.5A3.5 3.5 0 1 1 9 5.5a3.5 3.5 0 0 1 0 7z" fill="#fff"/></svg></div>
    <div><h4>Location</h4><p>48 Linden Row C Block<br>Suite 310 USA</p></div>
  </div>

  <div class="abs field" style="left:489px;top:103px;width:272px;height:42px">First Name</div>
  <div class="abs field" style="left:770px;top:103px;width:272px;height:42px">Last Name</div>
  <div class="abs field" style="left:489px;top:155px;width:272px;height:43px">Phone Number</div>
  <div class="abs field" style="left:770px;top:155px;width:272px;height:43px">Email Address</div>
  <div class="abs field" style="left:489px;top:207px;width:553px;height:117px">Message</div>
  <a class="btn" style="left:489px;top:334px;width:174px;height:43px">Send Message</a>
</section>

<footer class="site-footer">
  <h2 class="abs w" style="left:158px;top:88px;font-size:27px;font-weight:600">Velka Haven</h2>
  <p class="abs w" style="left:158px;top:151px;font-size:14.5px">Opening Hours</p>
  <div class="hours">
    <span class="lbl" style="left:158px;top:186px">MON - THUR :</span><span style="left:281px;top:185px">5am to 9pm</span>
    <span class="lbl" style="left:158px;top:217px">FRIDAY :</span><span style="left:281px;top:216px">5am to 7pm</span>
    <span class="lbl" style="left:158px;top:246px">SAT - SUN :</span><span style="left:281px;top:245px">7am to 2pm</span>
  </div>
  <p class="abs w" style="left:158px;top:324px;font-size:14.5px">Get In Touch</p>
  <div class="abs mail">Enter Your mail Id</div>
  <div class="abs mail-go"><svg width="14" height="14" viewBox="0 0 14 14"><path d="M1 6l12-5-5 12-1.5-5.5z" fill="#fff"/></svg></div>

  <p class="abs foot-h" style="left:458px;top:92px">Quick Link</p>
  <ul class="links">
    <li style="left:487px;top:152px">Home</li>
    <li style="left:487px;top:181px">About</li>
    <li style="left:487px;top:211px">Classes</li>
    <li style="left:487px;top:240px">Contact</li>
  </ul>
  <p class="abs foot-h" style="left:616px;top:92px">Classes</p>
  <ul class="links">
    <li style="left:640px;top:152px">Lorem Ipsum</li>
    <li style="left:640px;top:181px">Contrary to popular</li>
    <li style="left:640px;top:211px">Lorem Ipsum</li>
    <li style="left:640px;top:240px">Contrary to popular</li>
  </ul>
  <p class="abs foot-h" style="left:833px;top:92px">Instagram</p>
  <div class="abs insta" role="img" aria-label="Grid of nine yoga class photos">
    <div></div><div></div><div></div><div></div><div></div><div></div><div></div><div></div><div></div>
  </div>
  <p class="abs center w" style="top:394px;font-size:13px">© All right reserved 2022 <span style="color:var(--green-light)">Velkahaven</span></p>
</footer>

<div class="abs bottom-bar" style="left:0;width:1200px">
  <span class="abs social" style="left:552px"></span>
  <span class="abs social" style="left:587px"></span>
  <span class="abs social" style="left:621px"></span>
</div>

</body>
</html>
```